Stationary Design needed for luxorious bespoke tailor

We need a design for our stationary items like businescards, letters, envelope and letter head / Signature for email. Our company "LE CORVAN" sells exclusively and luxourious bespoke garments and accessories for men. The desgins of letterhead, envelope and business card shoulderstand communicate luxury, high quality and good taste. We would like our logo to be used on the designs.

Target Market(s)

Gentleman with a high aproach and exclusive and luxourious suits and shirts, grooms, businesman,

Industry/Entity Type

It Company

Font styles to use
Sans Serif

Colors
ec1f27
ffffff

Requirements
Must have
• Logo, Companies name and adress, contactName internet & email, phone number line / mobile, VAT Nr. On Business Card frontpage only logo and name, adress companies on backpage. No VAT and Companies ID there. Company data; LE CORVAN AG Wiesenrain 42 4057 Basel Switzerland VAT: CHE 472 916 304 Tax Tel 41 61 594 17 36 Mobile 41 79 842 06 91 www.korvanmode.ch info@korvanmode.com.
Nice to have
• -Name And phone numbers need to be able to change (for different coworkers ...)
Should not have
• no VAT in Business Card

```html
<!DOCTYPE html>
<html lang="de">
<head>
<meta charset="utf-8">
<title>LE CORVAN – Geschäftsausstattung</title>
<link rel="stylesheet" href="https://fonts.googleapis.com/css2?family=Montserrat:wght@400;500;600&display=swap">
<style>
  :root {
    --ink: #1a1a1a;
    --black: #0b0b0b;
    --white: #ffffff;
    --red: #ec1f27;
    --backdrop: #e6e6e6;
    --muted: #6d6d6d;
    --paper-shadow: 0 2px 10px rgba(0,0,0,0.12);
  }
  * { box-sizing: border-box; margin: 0; padding: 0; }
  html, body {
    width: 1200px; height: 789px; overflow: hidden;
    background: var(--backdrop);
    font-family: "Montserrat", Arial, sans-serif;
    color: var(--ink);
  }
  .sheet {
    position: absolute;
    background: var(--white);
    box-shadow: var(--paper-shadow);
  }

  /* wordmark */
  .wordmark {
    display: inline-flex; align-items: center; gap: 0.45em;
    font-weight: 600; letter-spacing: 0.14em; white-space: nowrap;
    color: var(--ink);
  }
  .wordmark .mark-square {
    width: 0.55em; height: 0.55em; background: var(--red); flex: none;
  }
  .wordmark--light { color: var(--white); }

  /* letterhead */
  .letterhead { left: 40px; top: 111px; width: 400px; height: 566px; padding: 34px 38px 0 44px; font-size: 6.4px; line-height: 1.55; }
  .letterhead .wordmark { position: absolute; right: 38px; top: 32px; font-size: 13px; }
  .recipient { margin-top: 62px; }
  .letter-date { margin-top: 18px; text-align: right; }
  .letter-subject { margin-top: 14px; font-weight: 600; }
  .letter-body p { margin-top: 9px; }
  .closing { margin-top: 16px; }
  .signature { display: block; margin-top: 8px; width: 78px; height: 22px; }
  .signer { color: var(--muted); }
  .letter-footer {
    position: absolute; left: 44px; right: 38px; bottom: 24px;
    border-top: 1px solid var(--red); padding-top: 6px;
    font-size: 5.2px; color: var(--muted); letter-spacing: 0.02em;
    display: flex; justify-content: space-between;
  }

  /* folder cover */
  .cover { left: 470px; top: 111px; width: 400px; height: 566px; background: var(--black); }
  .cover .wordmark { position: absolute; left: 50%; top: 44%; transform: translate(-50%, -50%); font-size: 34px; }
  .cover-url { position: absolute; left: 0; right: 0; bottom: 40px; text-align: center; font-size: 7px; color: #bdbdbd; letter-spacing: 0.1em; }

  /* envelope */
  .envelope { left: 900px; top: 111px; width: 260px; height: 130px; padding: 14px 16px; }
  .envelope .wordmark { font-size: 9px; }
  .return-address { margin-top: 5px; font-size: 5px; line-height: 1.5; color: var(--muted); }
  .envelope-rule { position: absolute; left: 16px; right: 16px; bottom: 14px; height: 1px; background: var(--red); }

  /* business cards */
  .card { width: 260px; height: 166px; left: 900px; }
  .card--front { top: 266px; background: var(--black); }
  .card--front .wordmark { position: absolute; left: 50%; top: 50%; transform: translate(-50%, -50%); font-size: 20px; }
  .card--back { top: 511px; padding: 20px 20px; }
  .card--back .wordmark { font-size: 12px; }
  .card-person { margin-top: 26px; font-size: 8px; font-weight: 600; letter-spacing: 0.04em; }
  .card-role { font-size: 6px; color: var(--muted); }
  .card-contacts {
    position: absolute; left: 20px; right: 20px; bottom: 16px;
    border-top: 1px solid var(--red); padding-top: 6px;
    font-size: 5.6px; line-height: 1.6; color: var(--muted);
    display: grid; grid-template-columns: 1fr 1fr;
  }
</style>
</head>
<body>

<section class="sheet letterhead" aria-label="Briefbogen">
  <div class="wordmark"><span>LE CORVAN</span><span class="mark-square"></span></div>
  <address class="recipient" style="font-style:normal">
    Herr Daniel Meier<br>Rheinweg 8<br>4058 Basel
  </address>
  <p class="letter-date">Basel, 12. März 2024</p>
  <p class="letter-subject">Ihre Massanfertigung</p>
  <div class="letter-body">
    <p>Sehr geehrter Herr Meier,</p>
    <p>vielen Dank für Ihren Besuch in unserem Atelier. Gerne bestätigen wir die Anfertigung Ihres Anzugs aus feiner italienischer Wolle, zugeschnitten nach Ihren persönlichen Massen.</p>
    <p>Die erste Anprobe ist in drei Wochen vorgesehen. Dabei prüfen wir Sitz, Länge und Schnitt und stimmen alle Details mit Ihnen ab.</p>
    <p>Für Fragen stehen wir Ihnen jederzeit gerne zur Verfügung.</p>
  </div>
  <p class="closing">Freundliche Grüsse</p>
  <svg class="signature" role="img" aria-label="Handschriftliche Unterschrift" viewBox="0 0 78 22">
    <rect width="78" height="22" fill="#ececec"/>
  </svg>
  <p>Marco Brunner</p>
  <p class="signer">President</p>
  <footer class="letter-footer">
    <span>LE CORVAN AG · Wiesenrain 42 · 4057 Basel</span>
    <span>T +41 61 594 17 36 · M +41 79 842 06 91</span>
    <span>info@korvanmode.com · CHE 472 916 304</span>
  </footer>
</section>

<section class="sheet cover" aria-label="Mappe">
  <div class="wordmark wordmark--light"><span>LE CORVAN</span><span class="mark-square"></span></div>
  <p class="cover-url">www.korvanmode.ch</p>
</section>

<section class="sheet envelope" aria-label="Briefumschlag">
  <div class="wordmark"><span>LE CORVAN</span><span class="mark-square"></span></div>
  <p class="return-address">LE CORVAN AG · Wiesenrain 42 · 4057 Basel</p>
  <div class="envelope-rule"></div>
</section>

<section class="sheet card card--front" aria-label="Visitenkarte Vorderseite">
  <div class="wordmark wordmark--light"><span>LE CORVAN</span><span class="mark-square"></span></div>
</section>

<section class="sheet card card--back" aria-label="Visitenkarte Rückseite">
  <div class="wordmark"><span>LE CORVAN</span><span class="mark-square"></span></div>
  <p class="card-person">Marco Brunner</p>
  <p class="card-role">Geschäftsführer</p>
  <div class="card-contacts">
    <span>LE CORVAN AG<br>Wiesenrain 42<br>4057 Basel</span>
    <span>T +41 61 594 17 36<br>M +41 79 842 06 91<br>info@korvanmode.com<br>www.korvanmode.ch</span>
  </div>
</section>

</body>
</html>
```